Professional Hairdresser needs powerful, clever, simple, modern business card

I need a professional, clever, powerful, bold, attractive, modern/simplistic business card.
I specialize in dimensional hair color, precision haircutting, modern classic design, and signature finishes.
I believe in advanced education, continued training with emphasis on perfect practice, and strive to be the best at what I do.
I am trained by the industry's best and have passion for what I do, I want my business card to reflect my talents, education, capabilities, signature color techniques and design and confidence.
I want to be known as reputable, bold, artistic, aware, classic yet modern, innovative, creative, dimensional, knowledgeable, and educated.
I want something bold, simple, elegant, modern, clever, and legible.
My personal style is progressive, modern, eclectic, clean with modern luxury comfort style.
I love the use of black and white, to creative visual interest and texture. I think putting black as a solid background with white bold font makes the words jump/glow to the eye. I also think a stark white background with bold black fonts looks great, maybe with a punch of red. It is simple, clean, elegant.
I have a QR code I would like to include on the card but have no idea how to make it visually pleasing or make sense.
I do not have a set logo and am not sure if this needs to be done first or if the business card should be done first.
Updates

Reason: Very difficult decision. All designers are amazing.

Reason: Difficult decisions

Reason: Need more time as yesterday was not able to work as much as possible with designers. They are all great and look forward to having time later to look at them.

Reason: Unexpected time delay.

Target Market(s)

Early 20's-mid 60's, female and male, fashion aware, people who can afford my prices, appreciate value

Industry/Entity Type

Training

Requirements
Must have
• I would like to incorporate the QR code I have if possible.
I would like to have my name and contact info.
I would like my logo (or maybe have my logo be RT in a font like listed below).
I would like the fonts to be modern, bold, clean, readable.
Fonts I have looked at are: The font used on the book called: Morvani An Age of Bright Shapes" I really love. I have looked at glyphwell.net for font and found "Georgiquas", but the designer wanted 200 euros which I just dont have at the time. Others I looked at include "Lin Libertine", Alien-Encounters-solid-regular-italic".
I love font used in the picture I included with the Tobias.Lindqvist ad.
Clean, modern, professional, legible, structured.
Nice to have
• I envision a black background with bold, modern, simple, font in white creating the effect of the words jumping off the card, visually apparent and glowing. Like a really expensive restaurant with a sign that you cant miss because the name is in bright white on black background, simple, bold, modern but not futuristic, powerful, clever, elegant, and draws the eye making it unforgetable. Perhaps layering black and white in order to where the font will be in white.
I see balance and chic.
Perhaps
Should not have
• I appreciate the trends in business design, but realize trends come and go and not sure if having something "trendy" is advisable for me. Having said that, I like creative modern design and sometimes current trends are important in design. I do like red as accent color, the primary blue color, blue on the PixelQuorum page, the masculine/florescent purple, and the neo bold yellow and the primary color shade of yellow.
I do not want clutter.
I do not want any fonts that are swirly, old-world calligraphy, script, or penmanship style.
I do not want picture of scissors, heads of old-school beauty school hair, or barber poles.

```html
<!DOCTYPE html>
<html lang="en">
<head>
<meta charset="utf-8">
<title>Rowan Tallis — Professional Hair</title>
<link href="https://fonts.googleapis.com/css2?family=Quicksand:wght@400;500;600&display=swap" rel="stylesheet">
<style>
  :root {
    --page: #2b2b2b;
    --card-deep: #070809;
    --card-glow: #1f2326;
    --text-main: #c9c9c9;
    --text-soft: #9a9a9a;
    --divider-dark: #000000;
    --divider-light: rgba(255,255,255,0.10);
    --icon: #a8a8a8;
  }
  html, body {
    margin: 0;
    padding: 0;
    width: 1200px;
    height: 1000px;
    overflow: hidden;
    background: var(--page);
  }
  .canvas {
    position: relative;
    width: 1200px;
    height: 1000px;
  }
  .card {
    position: absolute;
    left: 257px;
    width: 673px;
    height: 368px;
    box-shadow: 0 6px 18px rgba(0,0,0,0.6);
    overflow: hidden;
  }
  .card--front {
    top: 107px;
    background: radial-gradient(ellipse 60% 70% at 48% 62%, var(--card-glow) 0%, #111315 45%, var(--card-deep) 100%);
  }
  .card--back {
    top: 532px;
    background: radial-gradient(ellipse 60% 70% at 50% 22%, var(--card-glow) 0%, #111315 45%, var(--card-deep) 100%);
  }
  .divider {
    position: absolute;
    left: 363px;
    width: 2px;
    background: linear-gradient(to bottom, transparent, var(--divider-dark) 30%, var(--divider-dark) 70%, transparent);
    box-shadow: 1px 0 0 var(--divider-light);
  }
  .card--front .divider { top: 100px; height: 190px; }
  .card--back .divider { top: 95px; height: 190px; }

  .identity {
    position: absolute;
    right: 330px;
    top: 160px;
    text-align: right;
    font-family: "Quicksand", sans-serif;
  }
  .identity__name {
    margin: 0;
    font-size: 31px;
    font-weight: 600;
    line-height: 30px;
    letter-spacing: 0;
    color: var(--text-main);
  }
  .identity__role {
    margin: 2px 0 0;
    font-size: 12px;
    font-weight: 500;
    letter-spacing: 1.2px;
    color: var(--text-soft);
  }
  .monogram {
    position: absolute;
    left: 382px;
    top: 132px;
    margin: 0;
    font-family: "Quicksand", sans-serif;
    font-weight: 500;
    font-size: 92px;
    line-height: 100px;
    letter-spacing: 0;
    color: var(--text-main);
  }

  .contact {
    position: absolute;
    right: 0;
    top: 128px;
    width: 673px;
    margin: 0;
    padding: 0;
    list-style: none;
  }
  .contact__item {
    position: relative;
    height: 28px;
  }
  .contact__text {
    position: absolute;
    right: 323px;
    top: 4px;
    font-family: "Quicksand", sans-serif;
    font-size: 13px;
    font-weight: 500;
    letter-spacing: 0.3px;
    color: var(--text-main);
    white-space: nowrap;
  }
  .contact__icon {
    position: absolute;
    left: 378px;
    top: 3px;
    width: 20px;
    height: 20px;
    fill: var(--icon);
  }
</style>
</head>
<body>
<main class="canvas">
  <section class="card card--front" aria-label="Card front">
    <div class="divider"></div>
    <div class="identity">
      <h1 class="identity__name">ROWAN TALLIS</h1>
      <p class="identity__role">PROFESSIONAL HAIR</p>
    </div>
    <p class="monogram">RT</p>
  </section>

  <section class="card card--back" aria-label="Card back">
    <div class="divider"></div>
    <ul class="contact">
      <li class="contact__item">
        <span class="contact__text">555 314 272</span>
        <svg class="contact__icon" viewBox="0 0 20 20" aria-hidden="true">
          <path d="M2 7c0-2 3-3 8-3s8 1 8 3v1.5h-4V7H6v1.5H2z"/>
          <path d="M5 9h10l2 7H3z"/>
        </svg>
      </li>
      <li class="contact__item">
        <span class="contact__text">4120 Harbor Lane Oakmont, CA 90817</span>
        <svg class="contact__icon" viewBox="0 0 20 20" aria-hidden="true">
          <path d="M10 1.5a5.5 5.5 0 0 0-5.5 5.5c0 4 5.5 11.5 5.5 11.5s5.5-7.5 5.5-11.5A5.5 5.5 0 0 0 10 1.5zm0 7.8a2.3 2.3 0 1 1 0-4.6 2.3 2.3 0 0 1 0 4.6z"/>
        </svg>
      </li>
      <li class="contact__item">
        <span class="contact__text">hello@rowantallis.com</span>
        <svg class="contact__icon" viewBox="0 0 20 20" aria-hidden="true">
          <path d="M1 5h18v1l-9 6-9-6z"/>
          <path d="M1 7.5l9 6 9-6V15H1z"/>
        </svg>
      </li>
      <li class="contact__item">
        <span class="contact__text">Chirpline.com/RowanTallis</span>
        <svg class="contact__icon" viewBox="0 0 20 20" aria-hidden="true">
          <circle cx="10" cy="10" r="7"/>
        </svg>
      </li>
    </ul>
  </section>
</main>
</body>
</html>
```